Tarvelo Web Design

We need a redesign of our current website www.tarvelo-example.com

THIS IS A DESIGN STAGE ONLY

We have attached details of the whole project for your understanding only

We do not want to change our Logo but do want to have a more modern and intuitive feel to the site.

The first stage is the design but we are also looking for a coder to take the site to the next level

Tarvelo has a current website that has been in operation for the past 6 years the design was based around the Saas self-service model and while functional does not meet Tarvelo needs with regard to the new positioning.

We are happy to stay in Joomla or will look at alternatives

The purpose of the redesign is to align the look and feel of the website to meet our current new brand position and to provide a access point for the delivery of new content from Blogs and white papers as well as a portal for information for our current users for gathering Tips and Tricks and access to additional resources to assist them to provide feedback and get support.

Tarvelo is Australia's only PPM (Project and Portfolio Management) software provider that caters to the needs of project managers and C-level executives looking for insights into the alignment of resources to business strategy and investment decisions.

As companies gain maturity in PPM there is a need for innovation and management of change beyond just implementation of tools this is why Tarvelo has evolved from being a SaaS to becoming a SwS (Software with Service) provider.

Tarvelo is recognized as the tool of choice amongst program and project managers that is able to provide the user with an intuitive reliable interface that is capable of evolving and maturing to meet and exceed client requirements.

We are able to provide people at the coalface with tools that enable them to manage resources, scope, time sheeting, issues, changes and risk with excellent reporting functionality.

For C-level executives we are able to provide Business Intelligence (BI) functionality and reporting by integrating the PPM data with other business management systems such as ERP and CRM to provide a insight beyond pure PPM reporting.

We are able to provide Project Management insights from years of experience working with our clients in developing solutions that are inline with the evolution that comes with change.

Please feel free to email me on colin.marsh@tarvelo-example.com if you require any further details. A Site map and a wire frame is available.

Competitor sites include

www.plonvar-example.com
www.quesmit-example.com
www.rodkane-example.com
www.sulvex-example.com
Updates

Hi All 

We are getting some great designs coming in and really appreciate all of your efforts.

Some feedback to you all is that we have a preference for cleaner designs that take into account comprehension ability. So reverse type to us looks good but doesnt always get the cut through.

We have to remember that this is a marketing site first and foremost so what we are looking for is the ability to engage with our audience and get them to start to explore. That is upto us to provide great content and what we want from the design is the ability to be be able to engage with our Audience.

For your consideration please review this info from our marketing plan

There are 3 main communication groups inthe sales process.

Users-        These are the peoplewho will be at the coal face inputting the data and using the product on adaily basis. It is key to provide them with an easy to use and functional toolthat is able to provide them with the information they are looking for easily andintuitively. They have the capacity to say yes and can push the sale decisionup the chain. They equally have the power to say No and stop the sales processin its tracks. They will have a opinion who or what they feel is the best ofbreed and will try to influence the process.

Users are split into two groups.

Group1- They will be diploma if not degree qualifiedwill be a mix of Male and female with majority aged 18 to 35 they are at thecareer development stage of their life cycle normally on an income 45k to 70kper annum. We would position these people very strongly in the “What is in itfor me”.

Group2- PM who has used a variety of tools and systemsover the years they will be pre disposed to one or more systems and has morethan likely been exposed to MSP. Usually in the 30 to 50 year old age rangewith extensive on the job experience.

KeyInfluencers- These are the people who while notactually utilizing the software need to receive information in the form ofreports etc from the system. They normally don’t have the capacity to say yesbut they most certainly can say no. They will have come from a PM or IT roleand have a strong understanding of the PM processes. Influencers will be 30 to50 years of age they are at the family development stage with strong demandsfrom work and family predominantly male but not exclusively. They would bedegree qualified and possibly have completed or looking at additional studies. Therewill be an emphasis on getting the job done right. They are very time poor and hardto communicate with and engage. While being time poor they have an affinitywith and understand the greater good.

DecisionMakers- These are our key decision makers whilethey may not have direct input into the system or processes they are at the endof the day the people who approve the expenditure.

There is a huge demand for this person’stime with a multitude of people from internal employees and management,suppliers, customers, the community and potential suppliers. They are oftentravelling and going from one subject matter to another meeting after meeting.They will be at the stage where children are gaining some independents or leftthe home, career is stabilized and a clear path is formed. They are very directand deal in the facts and figures when it comes to decision making, they arenormally highly educated to the MBA or Doctorate level. They will be driven byoutcomes not the process of getting there.

 

A consistent theme across this group isthe following.

Psychographics

·Values time and considers ittheir single most limited resource.

·Excited about accepting andusing innovative ideas and products always wants to be at the fore front.

·Value adding has priority overprice

·Consistent web users: preferinternet over magazines and newspapers

Behavior

·They are leaders in productselection and respond to the opinions of the ‘Industry Experts’ when makingpurchase decisions.

·This group will look to theinternet to acquire the information

·Will make an informed decisionto purchase after due consideration.

·This group can be a powerfulsales force resulting from the referral network they build and use

Hope this helps

Hi All

Sorry for the delay we are in the final stages of decisions, so sorry we have had people away from the office who need to be involved in the process.

We will submit individual questions to those in the running and let all of the people who didnt get through this time as to why shortly.

We would like to thank you all for your efforts and submissions.

Regards

Colin Marsh 

Industry/Entity Type

Business Management

Requirements
Must have
• The scope of the website is to provide a modern functional website that is easy to navigate and provides a range of products and services to meet the needs of our potential clients and current users.

Two potential groups of viewers exist:
1. Potential Clients and users from the Project management community these would be split into 3 distinct groups. ( Please refer to Page 20 Tarvelo marketing Plan)
a. Project Managers
b. Project Directors
c. Business Managers
2. Current Tarvelo Users

The goal of website is to engage with the project management community reinforcing the Tarvelo Brand as Software with Service the key ethos should be around the company being thought leaders and industry experts with a strong commitment to clients and the success of their Portfolio/Program Management Office

Maintaining a modern and user friendly site is of the highest importance in order to hold users attention and guide the viewer to information that will lead to a decision to pursue accreditation and association with the Tarvelo Brand

We would like to guide potential clients to want to engage with us in assisting them to understand their current position in the P3M3 maturity model and to use us as a source for information and guidance.

Benefits for using the site should include:
• Information from a broad spectrum of Project Management professionals and recognized industry experts.
• Information on the Tarvelo Product and Services
• Timely and up to date information that encourages readers to return to the site
• Call to action, and plans for potential users of Tarvelo software.
• Demonstrate the benefits of accreditation and Call to action for current users to gain accreditation.
• Call to action for attending monthly webinars
• Ability to review past webinars, whitepapers etc.

```html
<!DOCTYPE html>
<html lang="en">
<head>
<meta charset="utf-8">
<title>Tarvelo – Project Management Software</title>
<link rel="stylesheet" href="https://fonts.googleapis.com/css2?family=Questrial&family=Arimo:wght@400;700&display=swap">
<style>
:root{
  --red:#e8402a;
  --ink:#2f2f2f;
  --text:#666666;
  --black:#0d0d0d;
  --white:#ffffff;
  --paper:#ffffff;
  --hero-warm:#f3d9cf;
  --hero-cool:#dfe4ea;
  --heading:"Questrial", "Century Gothic", sans-serif;
  --body:"Arimo", Arial, sans-serif;
}
*{margin:0;padding:0;box-sizing:border-box}
html,body{width:1050px;height:1200px;overflow:hidden;background:var(--paper)}
body{position:relative;font-family:var(--body);color:var(--text)}
a{color:inherit;text-decoration:none}
ul{list-style:none}

.top-rule{position:absolute;left:0;top:0;width:1050px;height:3px;background:var(--red)}

.util-links{position:absolute;right:166px;top:14px;font-size:10px;color:var(--text);display:flex;gap:6px}
.util-links .sep{color:#aaa}

.brand{position:absolute;display:flex;align-items:center;gap:8px;font-family:var(--heading);color:var(--ink);white-space:nowrap}
.brand .dot{width:14px;height:14px;border-radius:50%;background:var(--red)}
.brand-header{left:176px;top:36px;font-size:38px;line-height:40px}
.brand-footer{left:716px;top:1024px;font-size:32px;line-height:36px}

.main-nav{position:absolute;top:47px;left:0;width:1050px;height:27px;font-family:var(--heading);font-size:15px;color:var(--ink)}
.main-nav a{position:absolute;top:0;line-height:27px;white-space:nowrap}
.main-nav .current{left:328px;width:72px;text-align:center;background:var(--red);color:var(--white)}

.divider{position:absolute;left:150px;width:750px;height:14px;background:radial-gradient(ellipse at 50% 0%,rgba(0,0,0,.14),rgba(0,0,0,0) 70%)}

.side-tab{position:absolute;top:270px;width:34px;height:78px;background:#2a2a2a}
.side-tab.left{left:0;border-radius:0 40px 40px 0}
.side-tab.right{right:0;border-radius:40px 0 0 40px}
.side-tab svg{position:absolute;top:32px}
.side-tab.left svg{left:8px}
.side-tab.right svg{right:8px}

.hero-art{position:absolute;left:216px;top:134px;width:372px;height:132px;background:linear-gradient(120deg,var(--hero-warm),#eef0e6 55%,var(--hero-cool))}
.product-shot{position:absolute;left:514px;top:114px;width:360px;height:240px;background:linear-gradient(180deg,#d9dde2,#eef1f4 60%,#c9c9c9)}

.tour-btn{position:absolute;left:325px;top:277px;width:167px;height:42px;border:2px solid #d6d6d6;background:var(--white);display:flex;align-items:center;gap:10px;padding-left:9px;font-family:var(--heading);font-size:17px;color:var(--ink);white-space:nowrap}
.tour-btn .play{flex:none;width:25px;height:25px;border-radius:50%;background:var(--black);display:flex;align-items:center;justify-content:center}

.hero-title{position:absolute;left:0;top:358px;width:1050px;text-align:center;font-family:var(--heading);font-weight:400;font-size:47px;color:var(--ink)}
.hero-strap{position:absolute;left:253px;top:407px;width:534px;height:27px;background:var(--red);color:var(--white);font-family:var(--heading);font-size:21px;line-height:27px;text-align:center;white-space:nowrap}
.slider-dots{position:absolute;left:495px;top:446px;display:flex;gap:9px}
.slider-dots i{width:8px;height:8px;border-radius:50%;background:#3a3a3a}
.slider-dots i.on{background:var(--red)}

.feature{position:absolute;top:480px;width:170px;text-align:center}
.feature .icon{width:86px;height:86px;margin:0 auto;border-radius:50%;background:var(--black);display:flex;align-items:center;justify-content:center}
.feature h3{margin-top:8px;font-family:var(--heading);font-weight:400;font-size:20px;line-height:22px;color:var(--ink)}
.feature p{margin-top:10px;font-size:10px;line-height:15px;color:var(--text);height:56px}
.btn-dark{display:inline-block;margin-top:10px;width:107px;height:21px;line-height:21px;background:var(--black);color:var(--white);font-size:10px;text-transform:uppercase}

.truth-band{position:absolute;left:0;top:732px;width:1050px;height:115px;background:linear-gradient(90deg,rgba(232,64,42,0),var(--red) 12%,var(--red) 88%,rgba(232,64,42,0));color:var(--white);text-align:center}
.truth-band h2{margin-top:12px;font-family:var(--heading);font-weight:400;font-size:22px}
.truth-band p{width:700px;margin:6px auto 0;font-size:12px;line-height:19px}

.cta{position:absolute;top:864px;width:220px}
.cta h2{font-family:var(--heading);font-weight:400;font-size:22px;color:var(--ink);text-align:center;white-space:nowrap}
.cta p{margin-top:5px;font-size:10px;line-height:15px;text-align:center}
.btn-red{display:block;margin:18px auto 0;height:21px;line-height:21px;background:var(--red);color:var(--white);font-size:10px;text-transform:uppercase;text-align:center}
.cta-list{margin-top:6px;margin-left:40px;font-size:10px;line-height:15px}
.cta-list li::before{content:"•";color:var(--red);margin-right:7px}

.foot-col{position:absolute;top:1019px}
.foot-col h4{font-family:var(--heading);font-weight:400;font-size:15px;color:var(--ink);margin-bottom:6px}
.foot-col li{font-size:10px;line-height:17.5px;color:#444}
.social{position:absolute;left:735px;top:1106px;display:flex;gap:9px}
.social i{width:11px;height:11px;border-radius:50%;background:var(--ink)}

.site-footer{position:absolute;left:0;top:1146px;width:1050px;height:54px;background:var(--black)}
.site-footer .legal{position:absolute;left:205px;top:19px;font-size:10px;color:#ddd}
.newsletter{position:absolute;left:668px;top:12px;width:180px;height:22px;border-radius:11px;background:var(--white);font-size:9.5px;color:#333;line-height:22px;padding-left:16px}
.newsletter .go{position:absolute;right:0;top:0;width:30px;height:22px;border-radius:0 11px 11px 0;background:var(--red);display:flex;align-items:center;justify-content:center}
</style>
</head>
<body>
<div class="top-rule"></div>

<header>
  <nav class="util-links">
    <a href="#">FAQ</a><span class="sep">|</span><a href="#">Download</a><span class="sep">|</span><a href="#">Customers</a><span class="sep">|</span><a href="#">About Us</a><span class="sep">|</span><a href="#">Login</a><span class="sep">|</span><a href="#">Contact Us</a>
  </nav>
  <a class="brand brand-header" href="#"><span class="dot"></span>tarvelo</a>
  <nav class="main-nav">
    <a class="current" href="#">HOME</a>
    <a href="#" style="left:420px">TOUR</a>
    <a href="#" style="left:482px">FEATURES</a>
    <a href="#" style="left:580px">PRICING</a>
    <a href="#" style="left:661px">SUPPORT &amp; TRAINING</a>
    <a href="#" style="left:829px">SIGN UP</a>
  </nav>
</header>
<div class="divider" style="top:96px"></div>

<section class="hero">
  <a class="side-tab left" href="#"><svg width="12" height="14" viewBox="0 0 12 14"><path d="M10 0 L0 7 L10 14 Z" fill="#9a9a9a"/></svg></a>
  <a class="side-tab right" href="#"><svg width="12" height="14" viewBox="0 0 12 14"><path d="M2 0 L12 7 L2 14 Z" fill="#9a9a9a"/></svg></a>
  <div class="hero-art" role="img" aria-label="Illustration of colourful feature icons for planning, people, time and documents"></div>
  <div class="product-shot" role="img" aria-label="Product screenshot of the project overview dashboard on a laptop"></div>
  <a class="tour-btn" href="#"><span class="play"><svg width="10" height="12" viewBox="0 0 10 12"><path d="M1 0 L10 6 L1 12 Z" fill="#fff"/></svg></span>TAKE A TOUR</a>
  <h1 class="hero-title">PROJECT MANAGMENT</h1>
  <div class="hero-strap">Simple, easy to use project management software</div>
  <div class="slider-dots"><i class="on"></i><i></i><i></i><i></i></div>
</section>
<div class="divider" style="top:466px"></div>

<section class="features">
  <article class="feature" style="left:169px">
    <div class="icon"><svg width="34" height="34" viewBox="0 0 34 34"><g fill="#fff"><circle cx="17" cy="17" r="11"/><rect x="14" y="1" width="6" height="8"/><rect x="14" y="25" width="6" height="8"/><rect x="1" y="14" width="8" height="6"/><rect x="25" y="14" width="8" height="6"/><rect x="14" y="1" width="6" height="8" transform="rotate(45 17 17)"/><rect x="14" y="25" width="6" height="8" transform="rotate(45 17 17)"/><rect x="1" y="14" width="8" height="6" transform="rotate(45 17 17)"/><rect x="25" y="14" width="8" height="6" transform="rotate(45 17 17)"/></g><circle cx="17" cy="17" r="5" fill="#0d0d0d"/></svg></div>
    <h3>PROJECT<br>MANAGMENT</h3>
    <p>Simple, easy to use project management software. Plan, Track and Improve your projects. Reduce costs and increase efficiency.</p>
    <a class="btn-dark" href="#">More details</a>
  </article>
  <article class="feature" style="left:363px">
    <div class="icon"><svg width="40" height="40" viewBox="0 0 40 40"><circle cx="20" cy="20" r="17" fill="none" stroke="#fff" stroke-width="3"/><path d="M20 20 L27 11" stroke="#fff" stroke-width="3" stroke-linecap="round"/><circle cx="20" cy="20" r="3" fill="#fff"/><g stroke="#fff" stroke-width="2"><path d="M20 6v4M34 20h-4M6 20h4"/></g></svg></div>
    <h3>TIMESHEETS<br>SOFTWARE</h3>
    <p>Powerful hosted project time and status collection. Track expenses and time. Have an audit trail on your time billing. Timesheet software</p>
    <a class="btn-dark" href="#">More details</a>
  </article>
  <article class="feature" style="left:535px">
    <div class="icon"><svg width="46" height="30" viewBox="0 0 46 30"><g fill="#fff"><circle cx="23" cy="8" r="6"/><path d="M12 30 Q12 16 23 16 Q34 16 34 30 Z"/><circle cx="10" cy="11" r="4.5"/><path d="M1 28 Q1 18 10 18 Q14 18 15 20 Q11 23 11 28 Z"/><circle cx="36" cy="11" r="4.5"/><path d="M45 28 Q45 18 36 18 Q32 18 31 20 Q35 23 35 28 Z"/></g></svg></div>
    <h3>RESOURCE<br>MANAGEMENT</h3>
    <p>Plan, manage and control work for your whole organisation or a single project. Resource management</p>
    <a class="btn-dark" href="#">More details</a>
  </article>
  <article class="feature" style="left:707px">
    <div class="icon"><svg width="38" height="30" viewBox="0 0 38 30"><g fill="none" stroke="#fff" stroke-width="3.5"><path d="M2 7 H10 L24 23 H31"/><path d="M2 23 H10 L24 7 H31"/></g><g fill="#fff"><path d="M30 1 L37 7 L30 13 Z"/><path d="M30 17 L37 23 L30 29 Z"/></g></svg></div>
    <h3>ISSUES, RISKS<br>AND CHANGE</h3>
    <p>Track and report on issues, risk and change. One click reports. issue management</p>
    <a class="btn-dark" href="#">More details</a>
  </article>
</section>

<section class="truth-band">
  <h2>TARVELO! AN EXCLAMATION USED TO EMPHASIZE THE TRUTH</h2>
  <p>Tarvelo Pty Ltd is an Australian company with a ‘can do’ attitude. We develop and host a comprehensive software as a service Project Management solution via the web. Tarvelo is suitable for any organisation wanting to effectively manage projects, resources, time, issues, risks, changes and costs to realise planned business benefits.</p>
</section>

<section class="calls">
  <div class="cta" style="left:155px">
    <h2>FREE TRIAL</h2>
    <p>30 Day free trial.&nbsp;&nbsp;&nbsp;&nbsp;No obligations.<br>Cancel anytime.</p>
    <a class="btn-red" href="#" style="width:105px">Sign up now</a>
  </div>
  <div class="cta" style="left:402px">
    <h2>TAKE A TOUR</h2>
    <ul class="cta-list">
      <li>Project Managment</li>
      <li>Time Sheets</li>
      <li>Resource Managment</li>
      <li>Issues, Risks and Change</li>
    </ul>
  </div>
  <div class="cta" style="left:662px">
    <h2>SEE IT IN ACTION</h2>
    <p>Login and see the power of Tarvelo<br>for yourself in our demo enviroment.</p>
    <a class="btn-red" href="#" style="width:126px">Click here to login</a>
  </div>
</section>
<div class="divider" style="top:986px"></div>

<footer>
  <nav class="foot-col" style="left:205px"><h4>CONNECT</h4><ul><li>Home</li><li>FAQ</li><li>Support &amp; Training</li><li>Contact Us</li></ul></nav>
  <nav class="foot-col" style="left:329px"><h4>ABOUT</h4><ul><li>Tour</li><li>Features</li><li>Pricing</li><li>Sign up</li></ul></nav>
  <nav class="foot-col" style="left:431px"><h4>NAVIGATE</h4><ul><li>Careers</li><li>Privacy Policy</li><li>Terms of Sale</li><li>Sitemap</li></ul></nav>
  <a class="brand brand-footer" href="#"><span class="dot"></span>tarvelo</a>
  <div class="social" aria-label="Social links"><i></i><i></i><i></i><i></i><i></i></div>
  <div class="site-footer">
    <p class="legal">© 2003 - 2012 tarvelo pty. ltd. All Rights Reserved</p>
    <div class="newsletter">Sign up for a newsletter<span class="go"><svg width="14" height="10" viewBox="0 0 14 10"><rect x="0.5" y="0.5" width="13" height="9" fill="#fff"/><path d="M0.5 0.5 L7 6 L13.5 0.5" fill="none" stroke="#e8402a" stroke-width="1.2"/></svg></span></div>
  </div>
</footer>
</body>
</html>
```